Kelvo Roofing & construction LLC

I need an interactive website for potential customers with roofing products that we install and information about the products we install. I also want a page where customers can write reviews through google and facebook and can also contact us at. I would also like to add more information with the winning designer and would pay more with the winning designer.

```html
<!DOCTYPE html>
<html lang="en">
<head>
<meta charset="utf-8">
<title>Kelvo Roofing &amp; construction LLC</title>
<link href="https://fonts.googleapis.com/css2?family=Montserrat:wght@500;600;700;800;900&family=Raleway:wght@400;500;600;700&display=swap" rel="stylesheet">
<style>
:root{
  --red:#d7000f;
  --navy:#1c3359;
  --ink:#1f2a44;
  --text:#6f7480;
  --light:#f1eff0;
  --footer:#131a2a;
  --footer-line:#2a3346;
  --white:#ffffff;
}
*{margin:0;padding:0;box-sizing:border-box}
html,body{width:1200px;height:4522px;overflow:hidden;background:var(--white)}
body{position:relative;font-family:"Raleway",sans-serif;color:var(--text)}
.abs{position:absolute}
.head-font{font-family:"Montserrat",sans-serif}

/* header */
.site-header{position:absolute;left:0;top:0;width:1200px;height:79px;background:var(--white)}
.brand{position:absolute;left:131px;top:16px;display:flex;align-items:center;gap:8px;font-family:"Montserrat",sans-serif;font-weight:800;color:var(--navy)}
.brand-mark{width:14px;height:14px;background:var(--red)}
.brand-name{font-size:21px;line-height:1;letter-spacing:1px}
.brand-sub{position:absolute;left:153px;top:42px;font-family:"Montserrat",sans-serif;font-weight:800;font-size:8px;color:var(--navy);letter-spacing:1.5px;text-transform:uppercase}
.nav a{position:absolute;top:30px;font-family:"Montserrat",sans-serif;font-weight:600;font-size:13px;color:var(--ink);text-decoration:none}
.header-phone{position:absolute;left:928px;top:27px;display:flex;align-items:center;gap:6px;font-family:"Montserrat",sans-serif;font-weight:700;font-size:17px;color:var(--red)}

/* hero */
.hero{position:absolute;left:0;top:79px;width:1200px;height:614px;background:linear-gradient(160deg,#2f4a4c 0%,#263436 45%,#1b2022 100%)}
.hero-title{position:absolute;left:131px;top:184px;font-family:"Montserrat",sans-serif;font-weight:900;font-size:49px;line-height:56px;letter-spacing:6px;color:var(--white);text-transform:uppercase}
.hero-text{position:absolute;left:131px;top:313px;width:520px;font-size:17px;line-height:29px;color:#e9eeee}
.btn-red{position:absolute;background:var(--red);color:var(--white);font-family:"Montserrat",sans-serif;font-weight:600;font-size:12px;display:flex;align-items:center;justify-content:center}
.hero-arrow{position:absolute;top:290px}
.hero-dots{position:absolute;left:570px;top:564px;display:flex;gap:6px}
.hero-dots span{width:16px;height:5px;background:var(--white)}
.hero-dots span:first-child{background:var(--red)}

/* about */
.photo{position:absolute}
.about-label{position:absolute;left:672px;top:782px;font-family:"Montserrat",sans-serif;font-weight:600;font-size:11px;color:var(--red);letter-spacing:.5px}
.about-title{position:absolute;left:670px;top:814px;font-family:"Montserrat",sans-serif;font-weight:800;font-size:29px;line-height:37px;color:var(--navy)}
.about-text{position:absolute;left:669px;top:910px;width:380px;font-size:12px;line-height:20px}
.feature{position:absolute;top:1044px;width:200px}
.feature h4{display:flex;align-items:center;gap:10px;font-family:"Raleway",sans-serif;font-weight:600;font-size:13px;color:var(--navy);margin-bottom:10px}
.feature p{font-size:9px;line-height:15px}

/* call band */
.call-band{position:absolute;left:0;top:1281px;width:1200px;height:101px;background:var(--red)}
.call-band p{position:absolute;left:131px;top:36px;font-family:"Montserrat",sans-serif;font-weight:500;font-size:21px;color:var(--white)}
.btn-white{position:absolute;left:945px;top:31px;width:123px;height:40px;background:var(--white);color:var(--red);font-family:"Montserrat",sans-serif;font-weight:600;font-size:12px;display:flex;align-items:center;justify-content:center}

/* products */
.products{position:absolute;left:0;top:1382px;width:1200px;height:512px;background:var(--light)}
.dotfield{position:absolute;background:rgba(160,170,190,.12)}
.section-title{position:absolute;left:0;width:1200px;text-align:center;font-family:"Montserrat",sans-serif;font-weight:800;font-size:34px;letter-spacing:3px;color:var(--navy)}
.products-sub{position:absolute;left:0;top:145px;width:1200px;text-align:center;font-size:13px;line-height:19px}
.product-card{position:absolute;top:218px;width:216px;height:201px;background:var(--white);padding:42px 28px 0 29px}
.product-card h3{font-family:"Montserrat",sans-serif;font-weight:700;font-size:14px;line-height:20px;color:var(--navy);margin-bottom:18px}
.product-card p{font-size:10px;line-height:16px}
.product-card .chev{position:absolute;right:26px;bottom:26px}
.product-card.active{background:var(--navy)}
.product-card.active h3,.product-card.active p{color:var(--white)}

/* projects */
.projects{position:absolute;left:0;top:1894px;width:1200px;height:690px;background:var(--white)}
.pager{position:absolute;top:154px;height:29px;font-family:"Montserrat",sans-serif;font-weight:600;font-size:11px;color:var(--white);display:flex;align-items:center;justify-content:center}
.project{position:absolute;top:213px;height:378px}
.project-cap{position:absolute;left:18px;bottom:18px;width:255px;height:66px;background:rgba(40,30,30,.55);padding:12px 0 0 14px;color:var(--white)}
.project-cap small{display:block;font-size:10px}
.project-cap strong{font-family:"Montserrat",sans-serif;font-weight:600;font-size:15px}

/* testimonials */
.testimonials{position:absolute;left:0;top:2584px;width:1200px;height:451px;background:var(--light)}
.quote-card{position:absolute;top:173px;width:335px;height:141px;background:var(--white);padding:24px 24px 0 60px}
.quote-card p{font-style:italic;font-size:14px;line-height:25px;color:#8b8f98}
.quote-mark{position:absolute;left:18px;top:26px;font-family:"Montserrat",sans-serif;font-weight:900;font-size:36px;line-height:1;color:#6f7480}
.quote-tail{position:absolute;top:314px;width:0;height:0;border-left:12px solid transparent;border-right:12px solid transparent;border-top:12px solid var(--white)}
.person{position:absolute;top:338px;display:flex;align-items:center;gap:10px}
.avatar{width:38px;height:38px;background:linear-gradient(135deg,#7fb7c9,#c65a70)}
.person b{display:block;font-family:"Montserrat",sans-serif;font-weight:700;font-size:14px;color:var(--ink)}
.person small{font-size:9px}
.t-dots{position:absolute;left:570px;top:396px;display:flex;gap:6px}
.t-dots span{width:16px;height:5px;background:#555b66}
.t-dots span:first-child{background:var(--red)}

/* calculator */
.calc-photo{position:absolute;left:0;top:3126px;width:716px;height:484px;background:linear-gradient(120deg,#2c2c2c,#8e8e8e 45%,#4a4a4a)}
.calc{position:absolute;left:595px;top:3170px;width:370px;height:396px;background:var(--navy);padding:22px 30px 0 29px;color:var(--white)}
.calc h2{font-family:"Raleway",sans-serif;font-weight:500;font-size:31px}
.calc .lead{font-size:12px;color:#c9d2e2;margin-top:2px}
.calc label{display:block;font-size:7px;letter-spacing:.5px;color:#8c9ab4;text-transform:uppercase;margin:18px 0 5px}
.select{height:28px;border:1px solid #4b5f84;display:flex;align-items:center;justify-content:space-between;padding:0 10px;font-size:10px}
.slider{position:relative;height:6px;background:var(--white);border-radius:3px;margin-top:14px}
.slider i{position:absolute;left:107px;top:-8px;width:22px;height:22px;border-radius:50%;background:var(--red)}
.total{display:flex;justify-content:space-between;align-items:center;margin-top:26px}
.total span{font-family:"Montserrat",sans-serif;font-weight:500;font-size:14px}
.total strong{font-family:"Montserrat",sans-serif;font-weight:500;font-size:21px}

/* contact */
.contact-title{position:absolute;left:233px;top:3797px;font-family:"Raleway",sans-serif;font-weight:500;font-size:30px;line-height:42px;color:var(--navy)}
.contact-text{position:absolute;left:233px;top:3913px;width:260px;font-size:14px;line-height:21px}
.call-now{position:absolute;left:233px;top:3958px;width:254px;text-align:center;font-size:14px;color:var(--ink)}
.call-phone{position:absolute;left:277px;top:3980px;display:flex;align-items:center;gap:8px;font-family:"Montserrat",sans-serif;font-weight:600;font-size:18px;color:var(--red)}
.field-label{position:absolute;font-size:7px;text-transform:uppercase;color:#7b7f88}
.field{position:absolute;border:1px solid #dcdde1;background:var(--white)}

/* footer */
.footer{position:absolute;left:0;top:4099px;width:1200px;height:423px;background:var(--footer);color:#8a93a6}
.info-box{position:absolute;top:76px;height:98px;border:1px solid var(--footer-line);display:flex;align-items:center;padding-left:26px;gap:24px}
.info-box h5{font-family:"Montserrat",sans-serif;font-weight:600;font-size:11px;color:var(--white);margin-bottom:4px}
.info-box p{font-size:9px;line-height:16px}
.socials{display:flex;gap:16px;margin-top:10px}
.socials span{width:10px;height:10px;border-radius:50%;background:#c7cdd8}
.fcol{position:absolute;top:199px;width:170px}
.fcol h6{font-family:"Montserrat",sans-serif;font-weight:600;font-size:10px;color:var(--white);margin-bottom:12px}
.fcol p{font-size:7.5px;line-height:13px}
.subscribe{margin-top:16px;width:164px;height:26px;background:#1e2638;display:flex;align-items:center;justify-content:space-between;padding:0 10px;font-size:7px;color:#c7cdd8}
.news{display:flex;gap:12px;margin-bottom:18px}
.news .thumb{width:29px;height:29px;background:linear-gradient(135deg,#c97a8a,#7a4a5a);flex:none}
.news b{display:block;font-weight:500;font-size:8px;color:#c7cdd8;line-height:12px}
.footer-bottom{position:absolute;left:235px;top:393px;width:735px;display:flex;justify-content:space-between;font-size:7px}
.footer-bottom nav span{margin-left:28px;color:#c7cdd8}
</style>
</head>
<body>

<header class="site-header">
  <div class="brand"><span class="brand-mark"></span><span class="brand-name">KELVO ROOFING</span></div>
  <div class="brand-sub">&amp; construction LLC</div>
  <nav class="nav">
    <a style="left:400px">Home</a>
    <a style="left:479px">Products</a>
    <a style="left:577px">Portfolio</a>
    <a style="left:674px">Shop</a>
    <a style="left:746px">Contact</a>
  </nav>
  <div class="header-phone">
    <svg width="16" height="16" viewBox="0 0 24 24"><path fill="#d7000f" d="M6.6 10.8a15.1 15.1 0 0 0 6.6 6.6l2.2-2.2c.3-.3.7-.4 1-.2 1.1.4 2.3.6 3.6.6.6 0 1 .4 1 1V20c0 .6-.4 1-1 1A17 17 0 0 1 3 4c0-.6.4-1 1-1h3.5c.6 0 1 .4 1 1 0 1.3.2 2.5.6 3.6.1.3 0 .7-.2 1z"/></svg>
    800-555-0142
  </div>
</header>

<section class="hero" role="img" aria-label="Dark photograph of pitched rooftops against an overcast teal sky">
  <h1 class="hero-title">We welcome you<br>to Kelvo Roofing</h1>
  <p class="hero-text">We can restore your roof to the original look. It must include a dedication and expertice&nbsp; to go further in serving our ustomer.</p>
  <div class="btn-red" style="left:131px;top:400px;width:123px;height:42px">Request Service</div>
  <svg class="hero-arrow" style="left:8px" width="20" height="30" viewBox="0 0 20 30"><path d="M16 4 5 15l11 11" fill="none" stroke="#d7000f" stroke-width="3"/></svg>
  <svg class="hero-arrow" style="left:1172px" width="20" height="30" viewBox="0 0 20 30"><path d="M4 4l11 11L4 26" fill="none" stroke="#d7000f" stroke-width="3"/></svg>
  <div class="hero-dots"><span></span><span></span><span></span></div>
</section>

<section class="about">
  <div class="photo" style="left:321px;top:777px;width:270px;height:349px;background:linear-gradient(160deg,#4fb3b5,#2a6f8a 60%,#1d3a5c)" role="img" aria-label="Curved glass office tower against a teal sky"></div>
  <div class="photo" style="left:135px;top:854px;width:281px;height:225px;background:linear-gradient(180deg,#2e64a4 0%,#3d73b0 55%,#b5502e 100%)" role="img" aria-label="Chimneys on a terracotta tiled roof under blue sky"></div>
  <div class="photo" style="left:196px;top:995px;width:232px;height:180px;background:linear-gradient(180deg,#8ab3d0 0%,#6f8f6a 40%,#c4502a 100%);box-shadow:0 8px 20px rgba(0,0,0,.2)" role="img" aria-label="Red tiled rooftops over a town with hills behind"></div>
  <div class="about-label">MARKET LEADER SINCE 2000</div>
  <h2 class="about-title">Integrity, Fortitude Beyond<br>Design &amp; Durability</h2>
  <p class="about-text">We continously seek between design and technology. For over a decade, we've helped businesses to craft honest, emotional experiences through strategy, brand development, graphic design, web design. Our team hand picked to provide the right balance of skills to work.</p>
  <div class="feature" style="left:668px">
    <h4><svg width="12" height="12" viewBox="0 0 12 12"><rect x="1.5" y="1.5" width="9" height="9" fill="none" stroke="#d7000f" stroke-width="1.5"/></svg>Contemporary</h4>
    <p>Modern roof design is included as the architectural elements that come with certain styles.</p>
  </div>
  <div class="feature" style="left:880px">
    <h4><svg width="12" height="12" viewBox="0 0 12 12"><path d="M2 11V6l4-4 4 4v5" fill="none" stroke="#d7000f" stroke-width="1.5"/></svg>Innovative</h4>
    <p>Modern roof design is included as the architectural elements that come with certain styles.</p>
  </div>
</section>

<section class="call-band">
  <p>We're on call 24/7 to react promptly to your roofing problems.</p>
  <div class="btn-white">Request Service</div>
</section>

<section class="products">
  <div class="dotfield" style="left:63px;top:0;width:210px;height:512px" role="img" aria-label="Faint dotted grid decoration"></div>
  <h2 class="section-title" style="top:86px">PRODUCTS</h2>
  <p class="products-sub">We take pride in perfection: pride by producing a<br>first-quality product in a highly efficient and cost-effective</p>
  <article class="product-card" style="left:131px">
    <h3>Color Coated Roof<br>Sheets</h3>
    <p>Modern roof design is included as the architectural elements that come with certain styles.</p>
    <svg class="chev" width="8" height="10" viewBox="0 0 8 10"><path d="M2 1l4 4-4 4" fill="none" stroke="#1c3359" stroke-width="2"/></svg>
  </article>
  <article class="product-card" style="left:372px">
    <h3>High Poly Carbonate<br>Sheets</h3>
    <p>Modern roof design is included as the architectural elements that come with certain styles.</p>
    <svg class="chev" width="8" height="10" viewBox="0 0 8 10"><path d="M2 1l4 4-4 4" fill="none" stroke="#1c3359" stroke-width="2"/></svg>
  </article>
  <article class="product-card active" style="left:612px">
    <h3>Colour Coated Roof<br>Accessories</h3>
    <p>Modern roof design is included as the architectural elements that come with certain styles.</p>
    <svg class="chev" width="8" height="10" viewBox="0 0 8 10"><path d="M2 1l4 4-4 4" fill="none" stroke="#ffffff" stroke-width="2"/></svg>
  </article>
  <article class="product-card" style="left:852px">
    <h3>“Z” , “C” &amp; Sigma<br>Purlins</h3>
    <p>Modern roof design is included as the architectural elements that come with certain styles.</p>
    <svg class="chev" width="8" height="10" viewBox="0 0 8 10"><path d="M2 1l4 4-4 4" fill="none" stroke="#1c3359" stroke-width="2"/></svg>
  </article>
</section>

<section class="projects">
  <div class="dotfield" style="left:927px;top:0;width:210px;height:690px" role="img" aria-label="Faint dotted grid decoration"></div>
  <h2 class="section-title" style="top:82px">LATEST PROJECTS</h2>
  <div class="pager" style="left:131px;width:71px;background:var(--navy)">‹ Prev</div>
  <div class="pager" style="left:209px;width:71px;background:var(--red)">Next ›</div>
  <div class="project" style="left:131px;width:292px;background:linear-gradient(180deg,#2f62a0 0%,#3a6ea8 60%,#a0472a 100%)" role="img" aria-label="Chimneys on a clay tile roof">
    <div class="project-cap"><small>Village Roof</small><strong>Poly Cargonate Sheet</strong></div>
  </div>
  <div class="project" style="left:440px;width:291px;background:linear-gradient(160deg,#b4b4b4,#6e6e6e 50%,#3c3c3c)" role="img" aria-label="Aerial view of apartment blocks with flat roofs">
    <div class="project-cap"><small>Village Roof</small><strong>Poly Cargonate Sheet</strong></div>
  </div>
  <div class="project" style="left:756px;width:291px;background:linear-gradient(180deg,#9a9a9a 0%,#5e5e5e 55%,#3a3a3a 100%)" role="img" aria-label="City skyline by the water under cloudy sky">
    <div class="project-cap"><small>Village Roof</small><strong>Poly Cargonate Sheet</strong></div>
  </div>
  <div class="project" style="left:1072px;width:128px;background:linear-gradient(135deg,#7a2a1c,#b5553a 50%,#5a1e14)" role="img" aria-label="Close-up of weathered red roof shingles">
    <div class="project-cap" style="width:128px"><small>Village Roof</small><strong>Poly Cargonate</strong></div>
  </div>
</section>

<section class="testimonials">
  <h2 class="section-title" style="top:74px">TESTIMONIALS</h2>
  <div class="quote-card" style="left:212px"><span class="quote-mark">“</span><p>Lorem ipsum dolor sit consctetur adipiscing elit. Se Integer lore quam, adipiscing in condimentum tristique vel, eleifend sed turpis.</p></div>
  <div class="quote-tail" style="left:224px"></div>
  <div class="quote-card" style="left:651px"><span class="quote-mark">“</span><p>Lorem ipsum dolor sit consctetur adipiscing elit. Se Integer lore quam, adipiscing in condimentum tristique vel, eleifend sed turpis.</p></div>
  <div class="quote-tail" style="left:950px"></div>
  <div class="person" style="left:212px"><div class="avatar" role="img" aria-label="Portrait photo of reviewer"></div><div><b>Marna</b><small>UI Designer, Norv Agency</small></div></div>
  <div class="person" style="left:822px;flex-direction:row-reverse;text-align:right"><div class="avatar" role="img" aria-label="Portrait photo of reviewer"></div><div><b>Teval</b><small>UI Designer, Pell Agency</small></div></div>
  <div class="t-dots"><span></span><span></span><span></span></div>
</section>

<div class="dotfield" style="left:927px;top:3035px;width:210px;height:395px" role="img" aria-label="Faint dotted grid decoration"></div>
<div class="calc-photo" role="img" aria-label="Black and white close-up of banknotes"></div>
<section class="calc">
  <h2>Cost Calculator</h2>
  <p class="lead">*for detailed quote use extended version</p>
  <label>Type of service</label>
  <div class="select">Completely replace of roof<svg width="8" height="6" viewBox="0 0 8 6"><path d="M1 1l3 3 3-3" fill="none" stroke="#fff" stroke-width="1.5"/></svg></div>
  <label>Location type</label>
  <div class="select">Home &amp; Residence<svg width="8" height="6" viewBox="0 0 8 6"><path d="M1 1l3 3 3-3" fill="none" stroke="#fff" stroke-width="1.5"/></svg></div>
  <label>Roofing material</label>
  <div class="select">Slates<svg width="8" height="6" viewBox="0 0 8 6"><path d="M1 1l3 3 3-3" fill="none" stroke="#fff" stroke-width="1.5"/></svg></div>
  <label>Approximate roof size sq.ft</label>
  <div class="slider"><i></i></div>
  <div class="total"><span>TOTAL AMOUNT</span><strong>$ 5,210.00</strong></div>
</section>

<section class="contact">
  <h2 class="contact-title">Have a Question<br>About Roofing?</h2>
  <p class="contact-text">Our specialist will contact you and tell you about the conditions.</p>
  <p class="call-now">Call Us Now</p>
  <div class="call-phone">
    <svg width="18" height="18" viewBox="0 0 24 24"><path fill="#d7000f" d="M6.6 10.8a15.1 15.1 0 0 0 6.6 6.6l2.2-2.2c.3-.3.7-.4 1-.2 1.1.4 2.3.6 3.6.6.6 0 1 .4 1 1V20c0 .6-.4 1-1 1A17 17 0 0 1 3 4c0-.6.4-1 1-1h3.5c.6 0 1 .4 1 1 0 1.3.2 2.5.6 3.6.1.3 0 .7-.2 1z"/></svg>
    800-555-0187
  </div>
  <span class="field-label" style="left:545px;top:3787px">Your name</span>
  <span class="field-label" style="left:770px;top:3787px">Your email</span>
  <div class="field" style="left:545px;top:3801px;width:197px;height:33px"></div>
  <div class="field" style="left:770px;top:3801px;width:195px;height:33px"></div>
  <span class="field-label" style="left:545px;top:3861px">How can we help you?</span>
  <div class="field" style="left:545px;top:3873px;width:420px;height:76px"></div>
  <div class="btn-red" style="left:545px;top:3975px;width:123px;height:40px">Send Message</div>
</section>

<footer class="footer">
  <div class="info-box" style="left:131px;width:299px">
    <svg width="24" height="24" viewBox="0 0 24 24"><path fill="#fff" d="M6.6 10.8a15.1 15.1 0 0 0 6.6 6.6l2.2-2.2c.3-.3.7-.4 1-.2 1.1.4 2.3.6 3.6.6.6 0 1 .4 1 1V20c0 .6-.4 1-1 1A17 17 0 0 1 3 4c0-.6.4-1 1-1h3.5c.6 0 1 .4 1 1 0 1.3.2 2.5.6 3.6.1.3 0 .7-.2 1z"/></svg>
    <div><h5>CONTACTS</h5><p>Don't Hesitate To Call Us : +1 800 555 0163<br>Email Us At : hello@kelvoroof.com</p></div>
  </div>
  <div class="info-box" style="left:452px;width:297px">
    <svg width="26" height="26" viewBox="0 0 24 24"><path fill="#fff" d="M12 2a7 7 0 0 0-7 7c0 5 7 13 7 13s7-8 7-13a7 7 0 0 0-7-7zm0 9.5A2.5 2.5 0 1 1 12 6.5a2.5 2.5 0 0 1 0 5z"/></svg>
    <div><h5>ADDRESS</h5><p>Orrin Building, Flat 12<br>418 Calder Street, Westmoor</p></div>
  </div>
  <div class="info-box" style="left:772px;width:296px">
    <svg width="26" height="24" viewBox="0 0 24 22"><path fill="#fff" d="M12 21 10.5 19.7C5.4 15.1 2 12 2 8.3A5.3 5.3 0 0 1 7.4 3c1.7 0 3.4.8 4.6 2.1A6.1 6.1 0 0 1 16.6 3 5.3 5.3 0 0 1 22 8.3c0 3.7-3.4 6.8-8.5 11.4z"/></svg>
    <div><h5>FOLLOW US</h5><div class="socials"><span></span><span></span><span></span><span></span><span></span><span></span></div></div>
  </div>

  <div class="fcol" style="left:235px">
    <h6>About Us</h6>
    <p>Kelvo is a roofing and building team that has served local homes and shops for many years, fixing, fitting and caring for roofs of every kind and size.</p>
    <div class="subscribe">Subscribe to Our Newsletter<span>›</span></div>
  </div>
  <div class="fcol" style="left:421px">
    <h6>Business Hours</h6>
    <p>Opening Days :<br>&nbsp;&nbsp;&nbsp;&nbsp;Monday – Friday : 9am to 20 pm<br>&nbsp;&nbsp;&nbsp;&nbsp;Saturday : 9am to 17 pm<br><br>Vacations :<br>&nbsp;&nbsp;&nbsp;&nbsp;All Sunday Days<br>&nbsp;&nbsp;&nbsp;&nbsp;All Official Holidays</p>
  </div>
  <div class="fcol" style="left:609px">
    <h6>Latest Tweets</h6>
    <p>@kelvo Kelvo is a roofing team which offers repair, fitting and care for homes and shops of all kinds.<br>2 hours ago<br><br>@kelvo New roof guide out now for home owners.<br>2 hours ago</p>
  </div>
  <div class="fcol" style="left:796px">
    <h6>Our News</h6>
    <div class="news"><div class="thumb" role="img" aria-label="News thumbnail photo"></div><div><b>HOME RENOVATIONS WITH MODERN STYLE</b><p>On : Feb 12, 2020</p></div></div>
    <div class="news"><div class="thumb" role="img" aria-label="News thumbnail photo"></div><div><b>TIPS FOR BUYING DREAM HOUSE</b><p>On : April 10, 2020</p></div></div>
  </div>

  <div class="footer-bottom">
    <div>Kelvo Roofing © All Rights Reserved. &nbsp;&nbsp;&nbsp;&nbsp;&nbsp;&nbsp;&nbsp;&nbsp;&nbsp;&nbsp;<span style="color:#c7cdd8">Privacy Policy · Terms of Use</span></div>
    <nav><span>About</span><span>Services</span><span>Gallery</span><span>Blog</span><span>Contact</span></nav>
  </div>
</footer>

</body>
</html>
```